Creative Business Card for my Sail Boat.. Tide & Time

Going to order PLASTIC business cards for my boat.. she is a sailing vessel catamaran named Tide & Time..

Target Market(s)

to impress other boaters with a unique designed plastic card

Contact Information for Business Card

S/V Tide & Time
Captain Owen Hartley
hartley@owen.example
Mobile/WhatsApp 1-555-318-7062
www.sailtideandtime.example

Requirements
Must have
• Cool colors. logo.. and info in Business Card Details.. Thanks! Utilize clear or cloudy plastic in design. Thanks

```html
<!DOCTYPE html>
<html lang="en">
<head>
<meta charset="utf-8">
<title>Tide &amp; Time — Business Card</title>
<link rel="stylesheet" href="https://fonts.googleapis.com/css2?family=Arimo:wght@400;700&display=swap">
<style>
  :root {
    --page-bg: #d8cab6;
    --plastic: rgba(244, 240, 232, 0.72);
    --plastic-edge: rgba(255, 255, 255, 0.85);
    --brown-dark: #4a1e0c;
    --brown-light: #6e3a22;
    --green-light: #35a650;
    --green-dark: #1f6f2c;
    --ink-light: #eee3d2;
    --logo-ink: #5a3422;
    --logo-dot: #2f9a45;
  }
  * { margin: 0; padding: 0; box-sizing: border-box; }
  html, body {
    width: 1200px; height: 897px; overflow: hidden;
    background: var(--page-bg);
    font-family: "Arimo", Arial, sans-serif;
  }
  .card {
    position: absolute; left: 80px; top: 163px;
    width: 1040px; height: 570px;
    border-radius: 30px;
    background: linear-gradient(135deg, var(--plastic), rgba(230, 222, 208, 0.6));
    border: 2px solid var(--plastic-edge);
    box-shadow: 0 18px 40px rgba(70, 50, 30, 0.25);
    overflow: hidden;
  }
  .card-panels { position: absolute; inset: 0; }
  .holder-name {
    position: absolute; left: 42px; top: 88px;
    font-size: 46px; font-weight: 700; color: var(--ink-light);
    line-height: 1; white-space: nowrap;
  }
  .holder-title {
    position: absolute; left: 42px; top: 148px;
    font-size: 26px; line-height: 1; color: var(--ink-light);
  }
  .contact-list {
    position: absolute; left: 42px; top: 370px;
    list-style: none; color: var(--ink-light); font-size: 27px;
  }
  .contact-item { display: flex; align-items: center; gap: 12px; height: 39px; white-space: nowrap; }
  .contact-icon { width: 22px; height: 22px; flex-shrink: 0; fill: var(--ink-light); }
  .brand {
    position: absolute; left: 620px; top: 192px; width: 370px;
    display: grid; grid-template-columns: 70px auto; column-gap: 14px;
    align-items: end;
  }
  .brand-name {
    grid-column: 1 / 3; grid-row: 1;
    font-size: 86px; font-weight: 700; line-height: 0.98;
    color: var(--logo-ink); white-space: nowrap;
  }
  .brand-name .line-two { padding-left: 84px; display: block; }
  .brand-dot {
    grid-column: 1; grid-row: 1; align-self: end; margin-bottom: 12px;
    width: 60px; height: 60px; border-radius: 50%; background: var(--logo-dot);
  }
</style>
</head>
<body>
  <div class="card">
    <svg class="card-panels" width="1040" height="570" viewBox="0 0 1040 570">
      <defs>
        <linearGradient id="brown-fill" x1="0" y1="0" x2="1" y2="0">
          <stop offset="0" stop-color="var(--brown-light)"/>
          <stop offset="1" stop-color="var(--brown-dark)"/>
        </linearGradient>
        <linearGradient id="green-fill" x1="0" y1="0" x2="0" y2="1">
          <stop offset="0" stop-color="var(--green-light)"/>
          <stop offset="1" stop-color="var(--green-dark)"/>
        </linearGradient>
      </defs>
      <path class="panel-brown" d="M0 0 H600 L545 220 Q530 276 470 276 H0 Z" fill="url(#brown-fill)"/>
      <path class="panel-green" d="M0 293 H500 Q545 293 560 345 L594 570 H0 Z" fill="url(#green-fill)"/>
    </svg>

    <h1 class="holder-name">Captain Owen Hartley</h1>
    <p class="holder-title">CEO / Owner</p>

    <ul class="contact-list">
      <li class="contact-item">
        <svg class="contact-icon" viewBox="0 0 24 24"><path d="M6.6 10.8a15 15 0 0 0 6.6 6.6l2.2-2.2c.3-.3.7-.4 1-.2 1.1.4 2.3.6 3.6.6.6 0 1 .4 1 1V20c0 .6-.4 1-1 1A17 17 0 0 1 3 4c0-.6.4-1 1-1h3.5c.6 0 1 .4 1 1 0 1.3.2 2.5.6 3.6.1.3 0 .7-.2 1z"/></svg>
        <span>555-318-7062</span>
      </li>
      <li class="contact-item">
        <svg class="contact-icon" viewBox="0 0 24 24"><path d="M2 5h20v14H2z M3.5 6.5 12 13l8.5-6.5" fill="none" stroke="var(--ink-light)" stroke-width="2"/></svg>
        <span>hartley@owen.example</span>
      </li>
      <li class="contact-item">
        <svg class="contact-icon" viewBox="0 0 24 24"><circle cx="12" cy="12" r="9" fill="none" stroke="var(--ink-light)" stroke-width="2"/><path d="M3 12h18M12 3c3 3 3 15 0 18M12 3c-3 3-3 15 0 18" fill="none" stroke="var(--ink-light)" stroke-width="1.6"/></svg>
        <span>www.sailtideandtime.example</span>
      </li>
    </ul>

    <div class="brand">
      <span class="brand-dot"></span>
      <span class="brand-name">Tide &amp;<span class="line-two">Time</span></span>
    </div>
  </div>
</body>
</html>
```